1.ターゲット層は30〜60代の投資家ですが、60代が多めです。

2.グローバルナビ含め、トップページ内のコンテンツは同じですが、各コンテンツの掲載箇所等にこだわりはありませんので自由にデザインして下さい。

3.コンテンツエリアは、2カラム(メイン・右ナビ)で
それぞれのサイズは下記になります。
・メイン:650px
・右ナビ:300px
(メインと右ナビの間が10px)

4.できるだけ幅広いデザインを頂きたいため、
デザインのイメージ等はこちらから指示致しません。
※ご不明点はご質問ください。

5.なおトップロゴは現行のものを利用しますのでデザインの必要ありません。
広告箇所も同じくデザインの必要はありません。
※デザインの必要が無い箇所は添付赤枠部分となります。
※広告はデザインに合わせて配置いたしますので広告箇所をご指定頂く必要はありませ

ご不明な点がありましたら、お気軽にご連絡ください。
http://tsukimado.jp/
3ページ
• イラストレーター形式 (.ai)
• フォトショップ形式 (.psd)
基本のフォントサイズも特に指定ございません。

当選者については、アイコンなどになる部分に関して、決定後、切り出しやすいように定義していただきます。

【契約上のご注意】
・採用対象となる方には当社フォーマットの契約書を締結させて頂きます。
※添付「クラウドソーシング向け業務委託契約書_提示締結用.pdf」
【10月21日追記】
提案数が1件しか集まっていないため、募集期間を1週間延長させました。

新期限:10/28

既にご提案頂いた方、当初の期限までにご提案頂く予定だった方は大変申し訳ございません。
もう暫くお待ち下さい。
たくさんのご提案をいただきありがとうございます。
お礼ご返信も間に合っておりませんが、ご返信していないご提案も
全て検討対象とさせて頂きますのでご安心ください。

今後のスケジュールに関しまして追記させて頂きます。
ご提案頂いたデザインを当社上層部に提出し社内検討をさせて頂きます。

上層部スケジュールを合わせて会議を実施・決定の流れになりますので、
日程調整等でもう暫くお時間を頂戴できればと存じます。

色合いや全体イメージを社内複数人による多数決により決定させていただきました。

たくさんのご応募ありがとうございました。
本件につきましては社内調整等、
選定まで時間がかかりましたことお詫びいたします。

また本コンペは3件の当選予定をしておりまして、
今回決定の1件以外に別途2名の方に個別にプロジェクト形式でご発注させていただいております。

```html
<!DOCTYPE html>
<html lang="ja">
<head>
<meta charset="utf-8">
<title>Tsukimado 株式ニュース</title>
<link href="https://fonts.googleapis.com/css2?family=Noto+Sans+JP:wght@400;700&display=swap" rel="stylesheet">
<style>
:root{
  --orange:#f08300;--orange-dark:#d96f00;--ink:#333;--muted:#888;--line:#ddd;
  --band:#2e2e2e;--card:#fff;--page:#f2f2f2;--up:#d9261c;--down:#1a7bd0;--blue:#1f5fa6;--btn:#555;
}
*{box-sizing:border-box;margin:0;padding:0}
html,body{width:1200px;height:3000px;overflow:hidden}
body{font-family:"Noto Sans JP",sans-serif;color:var(--ink);background:var(--page);font-size:13px}
.wrap{width:960px;margin:0 auto;position:relative}
.site-header{background:#fff;height:72px}
.site-header .wrap{display:flex;align-items:center;justify-content:space-between;height:72px}
.brand{display:flex;align-items:center;gap:8px;font-weight:700;font-size:24px;color:var(--orange)}
.brand i{width:22px;height:22px;background:var(--orange);display:block}
.brand small{display:block;font-size:10px;color:var(--muted);font-weight:400}
.search{display:flex;align-items:center;gap:10px;font-size:12px}
.search .btn-s{background:var(--orange);color:#fff;padding:5px 12px;border-radius:3px}
.search input{width:140px;height:26px;border:1px solid var(--line);padding:0 8px}
.gnav{background:#fff;border-top:1px solid #eee;border-bottom:3px solid var(--orange)}
.gnav ul{display:flex;list-style:none}
.gnav li{flex:1;text-align:center;padding:12px 0;font-weight:700;font-size:14px;border-right:1px solid #eee}
.gnav li.on{background:var(--orange);color:#fff}
.ticker{background:var(--band);padding:24px 0}
.ticker .wrap{display:flex;gap:16px}
.idx{flex:1;background:#fff;border-radius:4px;padding:10px 14px}
.idx h3{font-size:12px;color:var(--muted);font-weight:400;display:flex;justify-content:space-between}
.idx .v{font-size:28px;font-weight:700;display:flex;align-items:center;gap:8px;margin:4px 0}
.idx .chg{font-size:12px;font-weight:700}
.up{color:var(--up)}.down{color:var(--down)}
.content{display:flex;gap:10px;margin-top:34px}
.main{width:650px}.side{width:300px}
.sec{background:#fff;border:1px solid var(--line);margin-bottom:30px;padding:18px 20px}
.sec-title{font-size:22px;font-weight:700;border-bottom:2px solid var(--orange);padding-bottom:8px;margin-bottom:14px;display:flex;align-items:baseline;gap:10px}
.sec-title::before{content:"";width:8px;height:22px;background:var(--orange);align-self:center}
.sec-title small{font-size:11px;color:var(--muted);font-weight:400}
.news-grid{display:flex;gap:16px}
.news-list{flex:1;list-style:none}
.news-list li{font-size:12px;padding:6px 0;border-bottom:1px dotted var(--line);white-space:nowrap;overflow:hidden}
.news-list li::before{content:"▶ ";color:var(--orange);font-size:9px}
.news-list time{color:var(--muted);margin-right:6px}
.chart-box{width:220px;border:1px solid var(--line);padding:6px;font-size:11px}
.more{display:inline-block;background:var(--blue);color:#fff;padding:6px 22px;border-radius:3px;font-size:12px;margin-top:8px}
.tags{display:flex;flex-wrap:wrap;gap:8px;margin-top:14px}
.tag{background:var(--btn);color:#fff;font-size:11px;padding:6px 12px;border-radius:3px}
.tag.on{background:var(--orange)}
table{width:100%;border-collapse:collapse;font-size:12px}
th{background:#f5f5f5;font-weight:400;color:var(--muted);padding:5px;text-align:left}
td{padding:6px 5px;border-bottom:1px solid #eee}
td.code{color:var(--blue)}
.pop{list-style:none;counter-reset:n}
.pop li{counter-increment:n;font-size:13px;padding:8px 0;border-bottom:1px dotted var(--line)}
.pop li::before{content:counter(n);display:inline-block;width:22px;height:22px;line-height:22px;text-align:center;background:var(--orange);color:#fff;font-weight:700;margin-right:10px;font-size:12px}
.disc li::before{content:"■";color:var(--blue);margin-right:6px}
.disc li{font-size:12px;padding:7px 0;border-bottom:1px dotted var(--line);list-style:none}
.disc a{color:var(--blue)}
.to-top{text-align:right}
.to-top span{display:inline-block;background:var(--blue);color:#fff;padding:10px 30px;font-weight:700;border-radius:4px 4px 0 0}
.rank{list-style:none}
.rank li{display:flex;gap:12px;padding:9px 0;border-bottom:1px solid #eee;font-size:13px}
.rank b{color:var(--orange);width:20px;text-align:center}
.side .sec{padding:14px 16px}
.side .sec-title{font-size:17px}
.site-footer{background:#fff;border-top:4px solid var(--orange);padding:26px 0;font-size:12px;text-align:center;color:var(--muted);line-height:1.9}
.site-footer nav{color:var(--ink);margin-top:10px}
.copy{background:var(--band);color:#bbb;text-align:center;padding:12px 0;font-size:11px}
</style>
</head>
<body>
<header class="site-header"><div class="wrap">
  <div class="brand"><i></i><div>Tsukimado<small>tsukimado.jp</small></div></div>
  <div class="search"><span class="btn-s">銘柄検索</span><label>○ テーマ</label><label>○ ニュース</label><input value="銘柄名・コード"></div>
</div></header>
<nav class="gnav"><div class="wrap"><ul>
  <li class="on">トップ</li><li>ニュース</li><li>決算速報</li><li>株価注意報</li><li>会社開示情報</li><li>市場マップ</li><li>銘柄検索</li>
</ul></div></nav>
<section class="ticker"><div class="wrap">
  <div class="idx"><h3>国内平均 <span>15:00</span></h3><div class="v down">▼ 15,138.96</div><div class="chg down">-56.81　-0.37%</div></div>
  <div class="idx"><h3>米ドル/円 <span>15:28</span></h3><div class="v up">▲ 107.96</div><div class="chg up">+1.01　0.94%</div></div>
  <div class="idx"><h3>新興総合 <span>15:00</span></h3><div class="v up">▲ 2,224.02</div><div class="chg up">+4.37　0.21%</div></div>
  <div class="idx"><h3>グロース指数 <span>15:00</span></h3><div class="v up">▲ 891.95</div><div class="chg up">+33.97　2.64%</div></div>
</div></section>

<div class="wrap content">
<main class="main">
  <section class="sec">
    <h2 class="sec-title">トップニュース<small>Top News</small></h2>
    <div class="news-grid">
      <ul class="news-list">
        <li>本日の相場スタート：円安進行で輸出関連株に買い</li>
        <li>【明日の好悪材料】本日の開示情報をチェック！</li>
        <li>★本日の【テクニカル】：上昇トレンド銘柄を抽出</li>
        <li>新興市場の動向：グロース指数が大幅続伸</li>
        <li>【注目】決算発表を控えた銘柄の値動きを点検</li>
        <li>小型株に資金流入、個人投資家の物色活発</li>
        <li>後場の相場展望：先物主導で底堅い動き</li>
        <li>為替動向：ドル円は108円台を試す展開に</li>
      </ul>
      <div class="chart-box">国内平均 日中足
        <svg width="206" height="140" viewBox="0 0 206 140"><g stroke="#eee"><line x1="0" y1="35" x2="206" y2="35"/><line x1="0" y1="70" x2="206" y2="70"/><line x1="0" y1="105" x2="206" y2="105"/></g><polyline fill="none" stroke="#1f5fa6" stroke-width="2" points="0,30 20,45 40,40 60,70 80,62 100,85 120,78 140,100 160,92 180,110 206,104"/></svg>
        <div style="text-align:center"><span class="more">相場概況を見る</span></div>
      </div>
    </div>
    <div class="tags"><span class="tag">市場概況を随時掲載</span><span class="tag">本日の注目テーマ</span><span class="tag">週間の騰落ランキング</span></div>
  </section>

  <section class="sec">
    <h2 class="sec-title">決算速報<small>Closing Bulletin</small></h2>
    <div class="news-grid">
      <ul class="news-list">
        <li><time>10/21 15:00</time>ミナト精機、今期経常を上方修正</li>
        <li><time>10/21 15:00</time>ソラノ電機、上期経常は2割増益</li>
        <li><time>10/21 14:30</time>アオバ技研、通期予想を据え置き</li>
        <li><time>10/21 14:00</time>ミナト精機、上期経常が計画上振れ</li>
        <li><time>10/21 13:30</time>ヒカリ通信、今期最終を増額修正</li>
        <li><time>10/21 13:00</time>カエデ商事、上期営業益が倍増</li>
      </ul>
      <div class="chart-box">決算発表件数
        <svg width="206" height="100" viewBox="0 0 206 100"><g fill="#f08300"><rect x="10" y="60" width="18" height="40"/><rect x="40" y="40" width="18" height="60"/><rect x="70" y="50" width="18" height="50"/><rect x="100" y="20" width="18" height="80"/><rect x="130" y="30" width="18" height="70"/><rect x="160" y="10" width="18" height="90"/></g></svg>
        <div style="text-align:center"><span class="more">一覧を見る</span></div>
      </div>
    </div>
    <div class="tags"><span class="tag">本日の決算発表予定</span><span class="tag">★本日の【テクニカル】</span><span class="tag">上方修正銘柄一覧</span><span class="tag">今週の決算発表予定</span></div>
  </section>

  <section class="sec">
    <h2 class="sec-title">ランキング・活況銘柄<small>Ranking &amp; Booming stock</small></h2>
    <div class="news-grid">
      <div style="flex:1">
        <div style="color:var(--blue);font-weight:700;margin-bottom:6px">▶ 上昇銘柄（本日 1部）</div>
        <table>
          <tr><th>順位</th><th>コード</th><th>銘柄名</th><th>株価</th><th>前日比</th><th>上昇率</th></tr>
          <tr><td>1</td><td class="code">3813</td><td>ミナト精機</td><td>356</td><td class="up">+80</td><td class="up">+14.89</td></tr>
          <tr><td>2</td><td class="code">4125</td><td>ソラノ電機</td><td>412</td><td class="up">+62</td><td class="up">+13.20</td></tr>
          <tr><td>3</td><td class="code">6231</td><td>アオバ技研</td><td>1,205</td><td class="up">+141</td><td class="up">+12.45</td></tr>
          <tr><td>4</td><td class="code">7312</td><td>ヒカリ通信</td><td>688</td><td class="up">+70</td><td class="up">+11.33</td></tr>
          <tr><td>5</td><td class="code">8419</td><td>カエデ商事</td><td>243</td><td class="up">+23</td><td class="up">+10.45</td></tr>
        </table>
      </div>
      <div class="chart-box">ミナト精機
        <svg width="206" height="150" viewBox="0 0 206 150"><g stroke="#eee"><line x1="0" y1="50" x2="206" y2="50"/><line x1="0" y1="100" x2="206" y2="100"/></g><polyline fill="none" stroke="#d9261c" stroke-width="2" points="0,130 25,120 50,125 75,95 100,100 125,70 150,60 175,40 206,25"/></svg>
        <div style="text-align:center"><span class="more">一覧を見る</span></div>
      </div>
    </div>
    <div class="tags"><span class="tag on">値上がり率</span><span class="tag">値下がり率</span><span class="tag">売買代金</span><span class="tag">出来高</span><span class="tag">年初来高値</span></div>
  </section>

  <section class="sec">
    <h2 class="sec-title">人気ニュースベスト10<small>Popular News</small></h2>
    <ul class="pop">
      <li>★本日の【テクニカル】：反発期待の銘柄（10/21）</li>
      <li>【注目】上期業績の上振れが期待される銘柄（10/21）</li>
      <li>【明日の好悪材料】を開示情報でチェック！（10/21）</li>
      <li>新興市場：グロース指数が大幅高（10/21）</li>
      <li>★本日の【テクニカル】：ゴールデンクロス銘柄（10/21）</li>
      <li>前場の相場展望：買い先行の展開（10/21）</li>
      <li>【注目】好業績の小型株を探る（10/21）</li>
      <li>為替動向：円安基調が続く（10/21）</li>
      <li>決算速報まとめ：上方修正が相次ぐ（10/21）</li>
      <li>週間の騰落ランキングを点検（10/21）</li>
    </ul>
  </section>

  <section class="sec">
    <h2 class="sec-title">開示情報<small>Disclosed information</small></h2>
    <ul class="disc">
      <li>10/21 15:00 <a>ミナト精機 業績予想の修正に関するお知らせ</a></li>
      <li>10/21 15:00 <a>ソラノ電機 第2四半期決算短信</a></li>
      <li>10/21 14:30 <a>アオバ技研 自己株式の取得状況に関するお知らせ</a></li>
      <li>10/21 14:00 <a>ヒカリ通信 配当予想の修正に関するお知らせ</a></li>
      <li>10/21 13:30 <a>カエデ商事 新株予約権の発行に関するお知らせ</a></li>
    </ul>
    <div style="text-align:right"><span class="more">一覧を見る</span></div>
  </section>
</main>

<aside class="side">
  <section class="sec">
    <h2 class="sec-title">検索ランキング</h2>
    <ol class="rank">
      <li><b>1</b>ソラノ電機</li><li><b>2</b>ミナト精機</li><li><b>3</b>アオバ技研</li>
      <li><b>4</b>ヒカリ通信</li><li><b>5</b>カエデ商事</li><li><b>6</b>ミナト精機</li>
    </ol>
  </section>
  <section class="sec">
    <h2 class="sec-title">指数一覧</h2>
    <svg width="266" height="170" viewBox="0 0 266 170"><rect width="266" height="170" fill="#fafafa"/><g stroke="#e5e5e5"><line x1="0" y1="42" x2="266" y2="42"/><line x1="0" y1="85" x2="266" y2="85"/><line x1="0" y1="128" x2="266" y2="128"/></g><polyline fill="none" stroke="#1f5fa6" stroke-width="2" points="0,40 30,55 60,50 90,80 120,72 150,95 180,90 210,115 240,108 266,125"/></svg>
    <table style="margin-top:10px">
      <tr><td>国内平均</td><td>15,138.96</td><td class="down">-56.81</td></tr>
      <tr><td>総合指数</td><td>1,245.40</td><td class="down">-3.12</td></tr>
      <tr><td>新興総合</td><td>2,224.02</td><td class="up">+4.37</td></tr>
      <tr><td>グロース指数</td><td>891.95</td><td class="up">+33.97</td></tr>
      <tr><td>米ドル/円</td><td>107.96</td><td class="up">+1.01</td></tr>
    </table>
    <div style="text-align:center"><span class="more">一覧を見る</span></div>
  </section>
  <section class="sec">
    <h2 class="sec-title">人気テーマ</h2>
    <ol class="rank">
      <li><b>1</b>電子部品</li><li><b>2</b>再生可能エネルギー</li><li><b>3</b>半導体</li>
      <li><b>4</b>リニア新幹線</li><li><b>5</b>ゲーム関連</li><li><b>6</b>人工知能</li>
      <li><b>7</b>自動運転</li><li><b>8</b>ロボット</li><li><b>9</b>インバウンド</li><li><b>10</b>宇宙開発</li>
    </ol>
    <div style="text-align:center"><span class="more">一覧を見る</span></div>
  </section>
</aside>
</div>

<div class="wrap to-top"><span>トップへ戻る ▲</span></div>
<footer class="site-footer">
  <p>本サイトの情報は投資判断の参考となる情報提供を目的としたものであり、投資勧誘を目的としたものではありません。</p>
  <p>掲載情報の正確性には万全を期しておりますが、その内容を保証するものではありません。</p>
  <nav>会社概要 ｜ 個人情報保護方針 ｜ サイトマップ ｜ 免責事項 ｜ 広告掲載 ｜ お問い合わせ ｜ 利用規約</nav>
</footer>
<div class="copy">Copyright © Tsukimado Inc. All Rights Reserved.</div>
</body>
</html>
```